looking to have a web site for the company which provides services in the industrial and commercial sectors such as: electrical, automation control and system integration, construction and maintenance, millwright, equipment assembly repair and installation. I have the domain already brivanholdings.net and logo. Most recent projects fulfilled for the following clients: MarlowKibbleCo, Dunholt University, OKSU, FALSTO, Tazzik, Prairie Grains

Target Market(s)

industrial and commercial sectors in electrical, automation, millwright and fabrication fields

Industry/Entity Type

Industrial

Coding

Coded - Design and coding required

Number of Pages Required

5+ page

Font styles to use
Sans Serif

Colors

Designer to choose colors to be used in the design.

Requirements
Nice to have
• looking to get something not complicated, nicely presented with minimum or no scrolling

```html
<!DOCTYPE html>
<html lang="en">
<head>
<meta charset="utf-8">
<title>Brivan Group Ltd — Industrial and Commercial Services</title>
<link rel="stylesheet" href="https://fonts.googleapis.com/css2?family=Montserrat:wght@400;500;600;700&family=Lato:wght@400;700&display=swap">
<style>
:root{
  --blue:#0d6aa8;
  --blue-dark:#0a5a91;
  --blue-band:rgba(14,98,170,.72);
  --ink:#2d2d2d;
  --grey-text:#7a7a7a;
  --bar:#3b3b3b;
  --light:#f2f2f2;
  --white:#ffffff;
  --card-dark:#262a2e;
}
*{margin:0;padding:0;box-sizing:border-box}
html,body{width:1200px;height:2727px;overflow:hidden}
body{position:relative;background:var(--white);font-family:'Lato',Arial,sans-serif;color:var(--ink)}
.abs{position:absolute}
.heading{font-family:'Montserrat',Arial,sans-serif;font-weight:700}

/* top bar */
.topbar{left:0;top:0;width:1200px;height:40px;background:var(--bar);color:var(--white)}
.topbar .call{left:74px;top:11px;font-size:14px;font-weight:700}
.topbar .call svg{position:absolute;left:-32px;top:-3px}
.social-dot{width:13px;height:13px;border-radius:50%;background:var(--white);display:block}
.topbar .socials{right:96px;top:13px;display:flex;gap:23px}

/* header */
.header{left:0;top:40px;width:1200px;height:105px;background:var(--white)}
.brand{font-family:'Montserrat',Arial,sans-serif;font-weight:700;letter-spacing:1px;color:var(--blue)}
.header .brand{left:67px;top:35px;font-size:30px;line-height:1}
.nav{top:41px;left:0;font-family:'Montserrat',Arial,sans-serif;font-size:15px;font-weight:500;color:var(--blue)}
.nav a{position:absolute;text-decoration:none;color:var(--blue);white-space:nowrap}
.nav .sep{position:absolute;width:1px;height:14px;background:#c9c9c9;top:3px}
.nav .active{background:var(--blue);color:var(--white);padding:2px 12px}

/* hero */
.hero{left:0;top:145px;width:1200px;height:704px;background:linear-gradient(90deg,#9aa3ab 0%,#c7ccd0 25%,#8d959c 45%,#b3b7b8 70%,#8a8a80 100%)}
.hero .sky{left:560px;top:0;width:640px;height:340px;background:linear-gradient(180deg,#d9dde0,#aab3bb)}
.hero .ground{left:0;top:600px;width:1200px;height:104px;background:linear-gradient(180deg,#9a8b78,#b7a893)}
.hero .band{left:0;top:373px;width:1200px;height:258px;background:var(--blue-band)}
.hero h1{left:100px;top:415px;font-size:64px;line-height:74px;color:var(--white);letter-spacing:1px}
.hero .sub{left:100px;top:562px;font-family:'Montserrat',Arial,sans-serif;font-weight:600;font-size:20px;color:var(--white);letter-spacing:.3px}

/* section titles */
.section-title{width:1200px;left:0;text-align:center;font-size:32px;letter-spacing:.5px}
.divider{left:309px;width:582px;height:30px}

/* about */
.about{left:0;top:849px;width:1200px;height:398px;background:var(--light)}
.about .section-title{top:48px;color:var(--blue)}
.about .copy{left:100px;top:165px;width:1000px}
.about .copy p{font-size:11.6px;line-height:14.5px;color:var(--grey-text);text-align:center;margin-bottom:18px}
.btn{display:flex;align-items:center;justify-content:center;gap:10px;height:31px;border-radius:16px;background:var(--blue);color:var(--white);font-family:'Montserrat',Arial,sans-serif;font-size:11px;font-weight:600}

/* services */
.services{left:0;top:1247px;width:1200px;height:671px;background:linear-gradient(135deg,#0d5f98 0%,#1a77b4 40%,#0e5d96 70%,#0b5286 100%)}
.services .section-title{top:56px;color:var(--white)}
.card{top:208px;width:286px;height:390px}
.card .photo{left:0;top:0;width:286px;height:176px}
.card .title{left:0;top:176px;width:286px;height:51px;background:var(--card-dark);color:#2f8fd1;font-size:18px;text-align:center;line-height:51px}
.card .body{left:0;top:227px;width:286px;height:163px;background:rgba(140,180,205,.45);color:var(--white);font-size:12.5px;line-height:15.5px;padding:12px 16px;text-align:justify}
.card .btn{position:absolute;left:79px;top:375px;width:128px}

/* blog + testimonials */
.lower{left:0;top:1918px;width:1200px;height:431px;background:var(--light)}
.lower h2{font-size:27px;color:var(--blue)}
.rule{height:1px;background:#a9a9a9}
.pager{display:flex;gap:4px}
.pager span{width:19px;height:19px;border-radius:50%;background:var(--blue);display:block}
.post{left:111px;width:460px;height:80px}
.post .thumb{left:0;top:0;width:78px;height:76px;background:linear-gradient(180deg,#8a8e93,#c9b9a9 55%,#6d7176)}
.post h3{left:93px;top:4px;font-size:16px;font-weight:700;color:var(--ink);font-family:'Lato',Arial,sans-serif}
.post p{left:93px;top:28px;width:370px;font-size:12.5px;line-height:16px;color:var(--ink)}
.post p.highlight{color:var(--blue)}
.post .date{left:93px;top:64px;font-size:12.5px;color:var(--ink)}
.testimonial .portrait{left:680px;top:156px;width:122px;height:124px;background:linear-gradient(180deg,#cfd6dc,#7f93a6)}
.testimonial .name{left:680px;top:299px;width:122px;text-align:center;font-family:'Montserrat',Arial,sans-serif;font-weight:700;font-size:13px;color:var(--blue)}
.testimonial .quote{left:822px;top:150px;width:312px;font-size:12.5px;line-height:16.3px;color:var(--ink);text-align:justify}
.testimonial .mark{color:var(--blue);font-family:Georgia,serif;font-size:22px;font-weight:700;line-height:0}

/* footer */
.footer{left:0;top:2349px;width:1200px;height:323px;background:var(--blue);color:var(--white)}
.footer .brand{left:76px;top:70px;color:var(--white);font-size:26px;line-height:29px}
.footer .about-text{left:76px;top:154px;width:250px;font-size:12px;line-height:14.5px}
.footer .vline{width:1px;top:70px;height:190px;background:rgba(255,255,255,.55)}
.footer h4{font-family:'Montserrat',Arial,sans-serif;font-weight:500;font-size:19px}
.footer .hr{height:1px;background:rgba(255,255,255,.5)}
.footer ul{list-style:none;font-size:14.5px;line-height:26.5px}
.footer li::before{content:"‹";margin-right:10px}
.footer .contact-lines{font-size:12px;line-height:22px}
.contact-row{display:flex;align-items:center;gap:6px}
.footer .accent{color:#5ec0f0}
.footer .phone-big{font-family:'Lato',Arial,sans-serif;font-size:24px}

.bottombar{left:0;top:2672px;width:1200px;height:55px;background:var(--bar);color:#d6d6d6;font-size:15px;text-align:center;line-height:55px}
</style>
</head>
<body>

<div class="abs topbar">
  <div class="abs call">
    <svg width="22" height="22" viewBox="0 0 22 22"><circle cx="11" cy="11" r="11" fill="#fff"/><path d="M7.5 6c.6-.4 1.2-.3 1.5.2l1 1.7c.3.5.2 1-.2 1.3l-.7.5c.6 1.3 1.6 2.3 2.9 2.9l.5-.7c.3-.4.9-.5 1.3-.2l1.7 1c.5.3.6.9.2 1.5-.6.9-1.6 1.2-2.6.8-2.6-1-4.6-3-5.6-5.6-.4-1 0-2 .8-2.6z" fill="#3b3b3b"/></svg>
    Call Us Free &nbsp;555-210-4470
  </div>
  <div class="abs socials"><span class="social-dot"></span><span class="social-dot"></span><span class="social-dot"></span><span class="social-dot"></span></div>
</div>

<header class="abs header">
  <div class="abs brand">BRIVAN GROUP LTD</div>
  <nav class="abs nav">
    <a class="active" style="left:624px;top:-2px">HOME</a>
    <span class="sep" style="left:708px"></span>
    <a style="left:722px">ABOUT US</a>
    <span class="sep" style="left:820px"></span>
    <a style="left:835px">SERVICES</a>
    <span class="sep" style="left:926px"></span>
    <a style="left:940px">BLOGS</a>
    <span class="sep" style="left:1013px"></span>
    <a style="left:1028px">CONTACT US</a>
  </nav>
</header>

<section class="abs hero">
  <div class="abs sky"></div>
  <div class="abs ground"></div>
  <div class="abs" role="img" aria-label="Photograph of industrial grain silos and a processing plant" style="left:0;top:0;width:1200px;height:704px"></div>
  <div class="abs band"></div>
  <h1 class="abs heading">INDUSTRIAL AND<br>COMMERCIAL SECTORS</h1>
  <div class="abs sub">IN ELECTRICAL, AUTOMATION, MILLWRIGHT AND FABRICATION FIELDS</div>
  <svg class="abs" style="left:22px;top:481px" width="18" height="30" viewBox="0 0 18 30"><path d="M15 3 4 15l11 12" fill="none" stroke="#fff" stroke-width="4"/></svg>
  <svg class="abs" style="left:1146px;top:481px" width="18" height="30" viewBox="0 0 18 30"><path d="m3 3 11 12L3 27" fill="none" stroke="#fff" stroke-width="4"/></svg>
</section>

<section class="abs about">
  <h2 class="abs heading section-title">ABOUT US</h2>
  <svg class="abs divider" style="top:105px" viewBox="0 0 582 30"><line x1="0" y1="22" x2="582" y2="22" stroke="#555" stroke-width="1.5"/><path d="M291 4 276 24h30z" fill="#0d6aa8"/><path d="M291 12l-7 10h14z" fill="#f2f2f2"/></svg>
  <div class="abs copy">
    <p>Lorem ipsum dolor sit amet, consectetur adipiscing elit. Quid autem habent admirationis, cum prope accesseris? An hoc usque quaque, aliter in vita? Non igitur de improbo, sed de callido improbo quaerimus, qualis Q. Nam quibus rebus efficiuntur voluptates, eae non sunt in potestate sapientis. Negare non possum. Huic mori optimum esse propter desperationem sapientiae, illi propter spem vivere. Quid enim me prohiberet Epicureum esse, si probarem, quae ille diceret? Qui-vere falsone, quaerere mittimus-dicitur oculis se privasse;</p>
    <p>Varietates autem iniurasque fortunae facile veteres philosophorum praeceptis instituta vita superabat. Et quod est munus, quod opus sapientiae? Non modo carum sibi quemque, verum etiam vehementer carum esse? Tu enim ista lenius, hic Stoicorum more nos vexat. Collatio igitur ista te nihil iuvat. Videamus animi partes, quarum est conspectus illustrior;</p>
  </div>
  <div class="abs btn" style="left:545px;top:307px;width:122px">READ MORE <svg width="12" height="14" viewBox="0 0 12 14"><path d="M1 0l10 7-10 7 3-7z" fill="#fff"/></svg></div>
</section>

<section class="abs services">
  <div class="abs" role="img" aria-label="Blue-tinted photograph of factory piping and machinery" style="left:0;top:0;width:1200px;height:671px"></div>
  <h2 class="abs heading section-title">SERVICES</h2>
  <svg class="abs divider" style="top:114px" viewBox="0 0 582 30"><line x1="0" y1="22" x2="582" y2="22" stroke="#fff" stroke-width="1.5"/><path d="M291 4 276 24h30z" fill="#fff"/><path d="M291 12l-7 10h14z" fill="#1570ad"/></svg>
  <svg class="abs" style="left:22px;top:309px" width="16" height="28" viewBox="0 0 16 28"><path d="M13 3 4 14l9 11" fill="none" stroke="#fff" stroke-width="3"/></svg>
  <svg class="abs" style="left:1148px;top:309px" width="16" height="28" viewBox="0 0 16 28"><path d="m3 3 9 11-9 11" fill="none" stroke="#fff" stroke-width="3"/></svg>

  <article class="abs card" style="left:105px">
    <div class="abs photo" role="img" aria-label="Photograph of a steel equipment assembly in a plant" style="background:linear-gradient(180deg,#6f6c68,#a9a49c 60%,#5d5a56)"></div>
    <div class="abs title heading">LOREM IPSUM</div>
    <div class="abs body">Lorem ipsum dolor sit amet, consectetur adipiscing elit. Quid autem habent admirationis, cum prope accesseris? An hoc usque quaque, aliter in vita? Non igitur de improbo, sed de callido improbo quaerimus, qualis Q. Nam quibus rebus efficiuntur voluptates, eae non sunt in</div>
    <div class="btn">READ MORE <svg width="12" height="14" viewBox="0 0 12 14"><path d="M1 0l10 7-10 7 3-7z" fill="#fff"/></svg></div>
  </article>

  <article class="abs card" style="left:464px">
    <div class="abs photo" role="img" aria-label="Photograph of stainless process tanks and piping" style="background:linear-gradient(180deg,#5a5753,#9d9890 55%,#4f4c48)"></div>
    <div class="abs title heading">LOREM IPSUM</div>
    <div class="abs body">Lorem ipsum dolor sit amet, consectetur adipiscing elit. Quid autem habent admirationis, cum prope accesseris? An hoc usque quaque, aliter in vita? Non igitur de improbo, sed de callido improbo quaerimus, qualis Q. Nam quibus rebus efficiuntur voluptates, eae non sunt in</div>
    <div class="btn">READ MORE <svg width="12" height="14" viewBox="0 0 12 14"><path d="M1 0l10 7-10 7 3-7z" fill="#fff"/></svg></div>
  </article>

  <article class="abs card" style="left:822px">
    <div class="abs photo" role="img" aria-label="Photograph of an electrical control panel with breakers" style="background:linear-gradient(180deg,#b8b6b2,#9a8f88 50%,#c9c4bd)"></div>
    <div class="abs title heading">LOREM IPSUM</div>
    <div class="abs body">Lorem ipsum dolor sit amet, consectetur adipiscing elit. Quid autem habent admirationis, cum prope accesseris? An hoc usque quaque, aliter in vita? Non igitur de improbo, sed de callido improbo quaerimus, qualis Q. Nam quibus rebus efficiuntur voluptates, eae non sunt in</div>
    <div class="btn">READ MORE <svg width="12" height="14" viewBox="0 0 12 14"><path d="M1 0l10 7-10 7 3-7z" fill="#fff"/></svg></div>
  </article>
</section>

<section class="abs lower">
  <h2 class="abs heading" style="left:102px;top:65px">LATEST BLOG</h2>
  <div class="abs pager" style="left:523px;top:73px"><span></span><span></span></div>
  <div class="abs rule" style="left:102px;top:122px;width:471px"></div>

  <div class="abs post" style="top:151px">
    <div class="abs thumb" role="img" aria-label="Thumbnail of an electrical panel"></div>
    <h3 class="abs">Verum tamen cum de rebus</h3>
    <p class="abs highlight">Lorem ipsum dolor sit amet, consectetur adipiscing elit. Quid utem habent admirationis,</p>
    <div class="abs date">10-Oct 2017</div>
  </div>
  <div class="abs post" style="top:261px">
    <div class="abs thumb" role="img" aria-label="Thumbnail of an electrical panel"></div>
    <h3 class="abs">Verum tamen cum de rebus</h3>
    <p class="abs">Lorem ipsum dolor sit amet, consectetur adipiscing elit. Quid utem habent admirationis,</p>
    <div class="abs date">10-Oct 2017</div>
  </div>

  <div class="abs" style="left:616px;top:64px;width:1px;height:291px;background:#b5b5b5"></div>

  <h2 class="abs heading" style="left:665px;top:65px">CLIENT TESTIMONIALS</h2>
  <div class="abs pager" style="left:1089px;top:73px"><span></span><span></span></div>
  <div class="abs rule" style="left:665px;top:122px;width:466px"></div>

  <div class="testimonial">
    <div class="abs portrait" role="img" aria-label="Portrait photo of the client"></div>
    <div class="abs name">DANIEL REYES</div>
    <p class="abs quote"><span class="mark">“</span> Lorem ipsum dolor sit amet, consectetur adipiscing elit. Quid autem habent admirationis, cum prope accesseris? An hoc usque quaque, aliter in vita? Non igitur de improbo, sed de callido improbo quaerimus, qualis Q. Nam quibus rebus efficiuntur voluptates, eae non sunt in potestate sapientis. Negare non possum. Huic mori optimum esse propter desperationem sapientiae, illi propter spem vivere. Quid enim me prohiberet Epicureum esse, si probarem, quae ille diceret <span class="mark">”</span></p>
  </div>
</section>

<footer class="abs footer">
  <div class="abs brand">BRIVAN<br>GROUP LTD</div>
  <p class="abs about-text">Lorem ipsum dolor sit amet, consectetur adipiscing elit. Quid autem habent admirationis, cum prope accesseris? An hoc usque quaque, aliter in vita? Non igitur de improbo, sed de callido improbo quaerimus.</p>

  <div class="abs vline" style="left:364px"></div>
  <div class="abs vline" style="left:584px"></div>
  <div class="abs vline" style="left:860px"></div>

  <h4 class="abs" style="left:404px;top:70px">QUICK LINKS</h4>
  <div class="abs hr" style="left:404px;top:104px;width:140px"></div>
  <ul class="abs" style="left:404px;top:118px">
    <li>Home</li><li>About us</li><li>Services</li><li>Blogs</li><li>Contact us</li>
  </ul>

  <h4 class="abs" style="left:629px;top:70px">CONTACT</h4>
  <div class="abs hr" style="left:629px;top:104px;width:196px"></div>
  <div class="abs contact-lines" style="left:629px;top:116px;line-height:16px">240 Kestrel Way<br>Fairmont, IL 60099</div>
  <div class="abs contact-lines" style="left:629px;top:164px">
    <div class="contact-row"><svg width="10" height="10" viewBox="0 0 10 10"><path d="M2 1c.4-.3.8-.2 1 .2l.7 1.1c.2.4.1.7-.2.9l-.4.3c.4.9 1.1 1.6 2 2l.3-.4c.2-.3.6-.4.9-.2l1.1.7c.4.2.5.6.2 1-.5.6-1.1.8-1.8.5C3.9 6.4 2.5 5 1.8 3.2 1.5 2.5 1.6 1.5 2 1z" fill="#fff"/></svg>555-210-4470</div>
    <div class="contact-row"><svg width="10" height="12" viewBox="0 0 10 12"><rect x="2" y="0.5" width="6" height="11" rx="1" fill="none" stroke="#fff"/><rect x="3.5" y="9" width="3" height="1" fill="#fff"/></svg>555-210-4471</div>
    <div class="contact-row"><svg width="10" height="8" viewBox="0 0 10 8"><rect x="0.5" y="0.5" width="9" height="7" fill="none" stroke="#fff"/><path d="M.5.5 5 4.5 9.5.5" fill="none" stroke="#fff"/></svg>contact@brivanholdings.net</div>
    <div class="contact-row"><svg width="10" height="10" viewBox="0 0 10 10"><circle cx="5" cy="5" r="4.5" fill="none" stroke="#fff"/><path d="M.5 5h9M5 .5c2 2.5 2 6.5 0 9M5 .5c-2 2.5-2 6.5 0 9" fill="none" stroke="#fff" stroke-width=".7"/></svg>www.brivanholdings.net</div>
  </div>

  <h4 class="abs" style="left:900px;top:73px;font-size:16px;font-weight:700">FOLLOW US <span class="accent">ON</span></h4>
  <div class="abs hr" style="left:900px;top:104px;width:196px"></div>
  <div class="abs" style="left:906px;top:129px;display:flex;gap:23px"><span class="social-dot"></span><span class="social-dot"></span><span class="social-dot"></span><span class="social-dot"></span></div>
  <div class="abs" style="left:907px;top:168px;width:18px;height:2px;background:#fff"></div>
  <div class="abs heading" style="left:907px;top:199px;font-size:15px">CALL US ON</div>
  <div class="abs phone-big" style="left:907px;top:219px">555-210-4470</div>
</footer>

<div class="abs bottombar">© 2017 brivan &nbsp;|&nbsp; Privacy Policy &nbsp;|&nbsp; User Agreement</div>

</body>
</html>
```